Urine collection cup with and without sterile seal sticker

Hello. We need a urine cup label designed please with

Name:
Date of Birth:
Date:
Time:
Temp℃:
Specimen ID:

Product code: TUB-47
Volume markings (e.g., 30 mL, 60 mL, 90 mL).
Vela Drug Tests logo

Could you please provide one version with the additional sterile sticker extending to the top, and one version without the additional sterile sticker?

```html
<!DOCTYPE html>
<html lang="en">
<head>
<meta charset="utf-8">
<title>Vela Drug Tests – Urine Cup Labels</title>
<link href="https://fonts.googleapis.com/css2?family=Roboto+Condensed:wght@500;700&display=swap" rel="stylesheet">
<style>
  :root {
    --navy: #0e3f8c;
    --ink: #123e7a;
    --band: #0d4a8a;
    --brand: #27a2e2;
    --paper: #ffffff;
    --page: #fdfdfd;
  }
  html, body {
    margin: 0;
    padding: 0;
    width: 1200px;
    height: 1200px;
    overflow: hidden;
    background: var(--page);
    font-family: "Roboto Condensed", "Arial Narrow", sans-serif;
  }
  .canvas { position: relative; width: 1200px; height: 1200px; }

  .label {
    position: absolute;
    box-sizing: border-box;
    height: 553px;
    background: var(--paper);
    border: 2.5px solid var(--navy);
    border-radius: 24px;
    overflow: hidden;
  }
  .label--sealed { left: 79px; top: 37px; width: 1045px; }
  .label--plain { left: 81px; top: 618px; width: 846px; }

  .brand { position: absolute; left: 31px; top: 37px; display: flex; align-items: center; gap: 12px; }
  .brand__dot { width: 72px; height: 72px; border-radius: 50%; background: var(--brand); }
  .brand__name { font-size: 58px; font-weight: 700; color: var(--brand); letter-spacing: 0.5px; line-height: 1; }

  .field {
    position: absolute;
    left: 35px;
    display: flex;
    align-items: flex-end;
    color: var(--ink);
    font-size: 34px;
    font-weight: 500;
    line-height: 1;
  }
  .field__line { border-bottom: 2px solid var(--ink); margin-left: 12px; margin-bottom: 3px; }
  .field--name { top: 156px; }
  .field--name .field__line { width: 467px; }
  .field--dob { top: 215px; }
  .field--dob .field__line { width: 368px; }
  .field--date { top: 274px; }
  .field--date .field__line { width: 480px; }
  .field--time { top: 334px; }
  .field--time .field__line { width: 195px; }
  .field--temp { top: 334px; left: 343px; }
  .field--temp .field__line { width: 138px; }
  .field--specimen { top: 393px; }
  .field--specimen .field__line { width: 375px; }

  .ref {
    position: absolute;
    left: 35px; top: 462px;
    width: 213px; height: 52px;
    box-sizing: border-box;
    border: 2px solid var(--ink);
    border-radius: 8px;
    display: flex; align-items: center;
    padding-left: 14px; gap: 16px;
    color: var(--ink);
  }
  .ref__tag {
    border: 2.5px solid var(--ink);
    font-size: 20px; font-weight: 700;
    padding: 2px 6px;
    line-height: 1;
  }
  .ref__code { font-size: 29px; font-weight: 700; }

  .scale { position: absolute; left: 660px; top: 60px; }
  .scale text { font-family: "Roboto Condensed", "Arial Narrow", sans-serif; fill: var(--ink); font-weight: 500; }

  .seal {
    position: absolute;
    left: 819px; top: 0;
    width: 224px; height: 100%;
    background: var(--band);
  }
  .seal__perforation {
    position: absolute;
    left: 8px; top: 6px; bottom: 6px;
    border-left: 2px dashed #ffffff;
  }
  .seal__word {
    position: absolute;
    left: 83px; top: 270px;
    transform: translate(-50%, -50%) rotate(-90deg);
    color: #ffffff;
    font-size: 56px; font-weight: 700;
    letter-spacing: 3px;
    line-height: 1;
  }
</style>
</head>
<body>
<div class="canvas">

  <!-- Label with sterile seal -->
  <section class="label label--sealed">
    <div class="brand"><span class="brand__dot"></span><span class="brand__name">Vela Drug Tests</span></div>
    <div class="field field--name"><span>Name:</span><span class="field__line"></span></div>
    <div class="field field--dob"><span>Date of Birth:</span><span class="field__line"></span></div>
    <div class="field field--date"><span>Date:</span><span class="field__line"></span></div>
    <div class="field field--time"><span>Time:</span><span class="field__line"></span></div>
    <div class="field field--temp"><span>Temp℃:</span><span class="field__line"></span></div>
    <div class="field field--specimen"><span>Specimen ID:</span><span class="field__line"></span></div>
    <div class="ref"><span class="ref__tag">REF</span><span class="ref__code">TUB-47</span></div>
    <svg class="scale" width="150" height="480" viewBox="0 0 150 480" aria-label="Volume scale">
      <g stroke="#123e7a" stroke-width="2.2">
        <line x1="11" y1="14" x2="11" y2="466"/>
        <line x1="11" y1="15" x2="45" y2="15"/><line x1="11" y1="35.5" x2="26" y2="35.5"/><line x1="11" y1="56" x2="26" y2="56"/><line x1="11" y1="76.5" x2="26" y2="76.5"/>
        <line x1="11" y1="97" x2="45" y2="97"/><line x1="11" y1="117.5" x2="26" y2="117.5"/><line x1="11" y1="138" x2="26" y2="138"/><line x1="11" y1="158.5" x2="26" y2="158.5"/>
        <line x1="11" y1="179" x2="45" y2="179"/><line x1="11" y1="199.5" x2="26" y2="199.5"/><line x1="11" y1="220" x2="26" y2="220"/><line x1="11" y1="240.5" x2="26" y2="240.5"/>
        <line x1="11" y1="261" x2="45" y2="261"/><line x1="11" y1="281.5" x2="26" y2="281.5"/><line x1="11" y1="302" x2="26" y2="302"/><line x1="11" y1="322.5" x2="26" y2="322.5"/>
        <line x1="11" y1="343" x2="45" y2="343"/><line x1="11" y1="363.5" x2="26" y2="363.5"/><line x1="11" y1="384" x2="26" y2="384"/><line x1="11" y1="404.5" x2="26" y2="404.5"/>
        <line x1="11" y1="425" x2="45" y2="425"/><line x1="11" y1="445.5" x2="26" y2="445.5"/><line x1="11" y1="465" x2="26" y2="465"/>
      </g>
      <text x="51" y="25" font-size="30">90 <tspan font-size="22">mL</tspan></text>
      <text x="51" y="189" font-size="30">60 <tspan font-size="22">mL</tspan></text>
      <text x="51" y="353" font-size="30">30 <tspan font-size="22">mL</tspan></text>
    </svg>
    <div class="seal">
      <span class="seal__perforation"></span>
      <span class="seal__word">STERILE</span>
    </div>
  </section>

  <!-- Label without sterile seal -->
  <section class="label label--plain">
    <div class="brand"><span class="brand__dot"></span><span class="brand__name">Vela Drug Tests</span></div>
    <div class="field field--name"><span>Name:</span><span class="field__line"></span></div>
    <div class="field field--dob"><span>Date of Birth:</span><span class="field__line"></span></div>
    <div class="field field--date"><span>Date:</span><span class="field__line"></span></div>
    <div class="field field--time"><span>Time:</span><span class="field__line"></span></div>
    <div class="field field--temp"><span>Temp℃:</span><span class="field__line"></span></div>
    <div class="field field--specimen"><span>Specimen ID:</span><span class="field__line"></span></div>
    <div class="ref"><span class="ref__tag">REF</span><span class="ref__code">TUB-47</span></div>
    <svg class="scale" width="150" height="480" viewBox="0 0 150 480" aria-label="Volume scale">
      <g stroke="#123e7a" stroke-width="2.2">
        <line x1="11" y1="14" x2="11" y2="466"/>
        <line x1="11" y1="15" x2="45" y2="15"/><line x1="11" y1="35.5" x2="26" y2="35.5"/><line x1="11" y1="56" x2="26" y2="56"/><line x1="11" y1="76.5" x2="26" y2="76.5"/>
        <line x1="11" y1="97" x2="45" y2="97"/><line x1="11" y1="117.5" x2="26" y2="117.5"/><line x1="11" y1="138" x2="26" y2="138"/><line x1="11" y1="158.5" x2="26" y2="158.5"/>
        <line x1="11" y1="179" x2="45" y2="179"/><line x1="11" y1="199.5" x2="26" y2="199.5"/><line x1="11" y1="220" x2="26" y2="220"/><line x1="11" y1="240.5" x2="26" y2="240.5"/>
        <line x1="11" y1="261" x2="45" y2="261"/><line x1="11" y1="281.5" x2="26" y2="281.5"/><line x1="11" y1="302" x2="26" y2="302"/><line x1="11" y1="322.5" x2="26" y2="322.5"/>
        <line x1="11" y1="343" x2="45" y2="343"/><line x1="11" y1="363.5" x2="26" y2="363.5"/><line x1="11" y1="384" x2="26" y2="384"/><line x1="11" y1="404.5" x2="26" y2="404.5"/>
        <line x1="11" y1="425" x2="45" y2="425"/><line x1="11" y1="445.5" x2="26" y2="445.5"/><line x1="11" y1="465" x2="26" y2="465"/>
      </g>
      <text x="51" y="25" font-size="30">90 <tspan font-size="22">mL</tspan></text>
      <text x="51" y="189" font-size="30">60 <tspan font-size="22">mL</tspan></text>
      <text x="51" y="353" font-size="30">30 <tspan font-size="22">mL</tspan></text>
    </svg>
  </section>

</div>
</body>
</html>
```